Luxury Business Card Design for High-End Window Treatments

Gilded Vantages
Custom Plantation Shutters & Architectural Shading Systems

⸻

BACK

Daniel Forsythe
Owner

Custom Interior & Exterior Window Treatments

919-482-7034
gildedvantages.com

I have included a picture that I’m hoping we can use on the back, but I’m also wondering if you can get rid of the ladder? Should we get rid of shutters , shades and blinds underneath Gilded Vantages?

Target Market(s)

High-end residential homeowners, custom home builders, architects, interior designers, and luxury renovation clients seeking premium plantation shutters and motorized architectural shading systems.

Industry/Entity Type

Custom Window treatments

Contact Information for Business Card

Front Gilded Vantages Custom Plantation Shutters Motorized Architectural Shading Systems BACK Daniel Forsythe Owner 919-482-7034 GildedVantages.com Custom Interior & Exterior Window Treatments By Appointment

Requirements
Nice to have
• Not 100% sure on nice to halves or the color but you can definitely check out my website to get a better understanding of what I’m trying to do

```html
<!DOCTYPE html>
<html lang="en">
<head>
<meta charset="utf-8">
<title>Gilded Vantages – Business Card</title>
<link rel="stylesheet" href="https://fonts.googleapis.com/css2?family=Poppins:wght@400;600;700&family=Marcellus&display=swap">
<style>
  :root {
    --page-bg: #e6e6e6;
    --card-black: #0b0b0b;
    --gold: #e8cd72;
    --gold-text: #d9b95c;
    --white: #ffffff;
    --ink: #111111;
    --photo-sky: #6f9fd6;
    --photo-wall: #3a3d44;
    --photo-trim: #d9d6cf;
    --photo-green: #3f5a33;
  }
  html, body {
    margin: 0;
    padding: 0;
    width: 1200px;
    height: 1200px;
    overflow: hidden;
    background: var(--page-bg);
    font-family: "Poppins", sans-serif;
  }
  .card {
    position: absolute;
    left: 155px;
    width: 890px;
    height: 506px;
    background: var(--card-black);
    overflow: hidden;
  }
  .card--front { top: 69px; }
  .card--back { top: 631px; }

  .front-shapes {
    position: absolute;
    inset: 0;
    width: 100%;
    height: 100%;
  }
  .headline {
    position: absolute;
    left: 62px;
    top: 62px;
    margin: 0;
    color: var(--white);
    font-weight: 700;
    font-size: 30px;
    line-height: 41px;
    text-transform: uppercase;
    letter-spacing: 0.2px;
  }
  .owner-name {
    position: absolute;
    left: 62px;
    top: 236px;
    margin: 0;
    color: var(--ink);
    font-weight: 600;
    font-size: 38px;
    line-height: 1;
  }
  .owner-role {
    position: absolute;
    left: 62px;
    top: 281px;
    margin: 0;
    color: var(--ink);
    font-weight: 400;
    font-size: 21px;
    line-height: 1;
  }
  .contact {
    position: absolute;
    left: 62px;
    margin: 0;
    display: flex;
    align-items: center;
    gap: 14px;
    color: var(--gold-text);
    font-size: 23px;
    line-height: 1;
  }
  .contact--phone { top: 373px; }
  .contact--web { top: 416px; }
  .contact-icon { width: 20px; height: 20px; flex: none; }

  .brand {
    position: absolute;
    left: 0;
    right: 0;
    top: 118px;
    text-align: center;
    color: var(--gold-text);
  }
  .brand-name {
    margin: 0;
    font-family: "Poppins", sans-serif;
    font-weight: 400;
    font-size: 64px;
    line-height: 76px;
  }
  .brand-tagline {
    margin: 22px 0 0;
    font-family: "Marcellus", serif;
    font-size: 31px;
    word-spacing: 14px;
    letter-spacing: 0.5px;
  }
</style>
</head>
<body>

<section class="card card--front">
  <svg class="front-shapes" viewBox="0 0 712 405" preserveAspectRatio="none" aria-hidden="false">
    <defs>
      <linearGradient id="porch-tones" x1="0" y1="0" x2="0" y2="1">
        <stop offset="0" stop-color="var(--photo-sky)"/>
        <stop offset="0.2" stop-color="var(--photo-trim)"/>
        <stop offset="0.3" stop-color="var(--photo-wall)"/>
        <stop offset="0.55" stop-color="var(--photo-wall)"/>
        <stop offset="0.7" stop-color="var(--photo-trim)"/>
        <stop offset="0.85" stop-color="var(--photo-green)"/>
        <stop offset="1" stop-color="#6b6357"/>
      </linearGradient>
    </defs>
    <polygon role="img" aria-label="Photo of a covered back porch fitted with dark exterior roll-down shades, with lawn chairs and shrubs in front"
             points="611,0 712,0 712,405 336,405" fill="url(#porch-tones)"/>
    <polygon class="stripe-white" points="531,0 571,0 336,405 309,405" fill="var(--white)"/>
    <polygon class="stripe-gold" points="571,0 611,0 498,140 456,140" fill="var(--gold)"/>
    <polygon class="stripe-gold-short" points="512,36 545,36 459,145 426,145" fill="var(--gold)"/>
    <polygon class="name-band" points="0,181 486,181 436,261 0,261" fill="var(--gold)"/>
  </svg>

  <h1 class="headline">Custom<br>Interior &amp; Exterior<br>Window Treatments</h1>
  <p class="owner-name">Daniel Forsythe</p>
  <p class="owner-role">Owner</p>

  <p class="contact contact--phone">
    <svg class="contact-icon" viewBox="0 0 24 24" aria-hidden="true">
      <path d="M6.6 10.8a15 15 0 0 0 6.6 6.6l2.2-2.2a1 1 0 0 1 1-.25 11.4 11.4 0 0 0 3.6.57 1 1 0 0 1 1 1V20a1 1 0 0 1-1 1A17 17 0 0 1 3 4a1 1 0 0 1 1-1h3.5a1 1 0 0 1 1 1c0 1.25.2 2.45.57 3.57a1 1 0 0 1-.25 1z" fill="var(--gold-text)"/>
    </svg>
    919-482-7034
  </p>
  <p class="contact contact--web">
    <svg class="contact-icon" viewBox="0 0 24 24" aria-hidden="true">
      <g fill="none" stroke="var(--gold-text)" stroke-width="2">
        <circle cx="12" cy="12" r="9"/>
        <ellipse cx="12" cy="12" rx="4" ry="9"/>
        <line x1="3" y1="12" x2="21" y2="12"/>
      </g>
    </svg>
    gildedvantages.com
  </p>
</section>

<section class="card card--back">
  <div class="brand">
    <p class="brand-name">Gilded<br>Vantages</p>
    <p class="brand-tagline">Shutters Shades Blinds</p>
  </div>
</section>

</body>
</html>
```